I need a cover for a brochure made

I need a cover for a brochure. The dimensions are 8.25 wide and 5.25 high... I also need a .25 inch bleed outside of those dimensions.

I need it to look like a vintage photo album cover. In big words, I would like it to say "Family". Above it in smaller words "To our Harlow Fairway" ... making it look like the words are gold inlay or something.

I would like it kind of in the style of some of the attached maybe. Just vintage looking.

```html
<!DOCTYPE html>
<html lang="en">
<head>
<meta charset="utf-8">
<title>Family – Harlow Fairway Brochure Cover</title>
<link rel="stylesheet" href="https://fonts.googleapis.com/css2?family=Merriweather:wght@900&family=Libre+Baskerville&display=swap">
<style>
  :root {
    --plum: #2d1a22;
    --plum-deep: #241419;
    --gold-dark: #a66b26;
    --gold-mid: #cf9a4e;
    --gold-light: #fde39c;
    --gold-line: #c48a3c;
  }
  html, body {
    margin: 0;
    padding: 0;
    width: 1200px;
    height: 764px;
    overflow: hidden;
    background: var(--plum);
  }
  .cover {
    display: block;
    width: 1200px;
    height: 764px;
  }
  .cover__title {
    font-family: "Merriweather", Georgia, serif;
    font-weight: 900;
    font-size: 212px;
  }
  .cover__dedication {
    font-family: "Libre Baskerville", Georgia, serif;
    font-weight: 400;
    font-size: 57px;
  }
  .frame-line {
    fill: none;
    stroke: var(--gold-line);
  }
</style>
</head>
<body>
<svg class="cover" viewBox="0 0 1200 764" xmlns="http://www.w3.org/2000/svg">
  <defs>
    <linearGradient id="gold-sheen" x1="170" y1="0" x2="1035" y2="0" gradientUnits="userSpaceOnUse">
      <stop offset="0" stop-color="var(--gold-dark)"/>
      <stop offset="0.5" stop-color="var(--gold-light)"/>
      <stop offset="1" stop-color="var(--gold-dark)"/>
    </linearGradient>
    <linearGradient id="border-gold" x1="0" y1="0" x2="1" y2="1">
      <stop offset="0" stop-color="#b07a32"/>
      <stop offset="0.5" stop-color="#d9a85a"/>
      <stop offset="1" stop-color="#b07a32"/>
    </linearGradient>
  </defs>

  <!-- background -->
  <rect class="cover__ground" width="1200" height="764" fill="var(--plum)"/>

  <!-- ornamental border band -->
  <path class="cover__border-band" role="img" aria-label="Ornate gold lace pattern border"
        fill="url(#border-gold)" fill-rule="evenodd" opacity="0.85"
        d="M30 25 H1168 V739 H30 Z M77 68 V697 H1122 V68 Z"/>
  <rect class="cover__inner-panel" x="77" y="68" width="1045" height="629" fill="var(--plum)"/>
  <rect class="frame-line" x="78" y="70" width="1046" height="625" stroke-width="1.5"/>

  <!-- inner frame lines -->
  <g class="frame-line" stroke-width="2">
    <line x1="244" y1="88" x2="956" y2="88"/>
    <line x1="244" y1="675" x2="956" y2="675"/>
    <line x1="97" y1="214" x2="97" y2="555"/>
    <line x1="1101" y1="214" x2="1101" y2="555"/>
    <!-- corner runners -->
    <line x1="150" y1="88" x2="236" y2="88"/>
    <line x1="964" y1="88" x2="1050" y2="88"/>
    <line x1="150" y1="675" x2="236" y2="675"/>
    <line x1="964" y1="675" x2="1050" y2="675"/>
    <line x1="97" y1="140" x2="97" y2="206"/>
    <line x1="1101" y1="140" x2="1101" y2="206"/>
    <line x1="97" y1="563" x2="97" y2="625"/>
    <line x1="1101" y1="563" x2="1101" y2="625"/>
  </g>

  <!-- corner flourishes -->
  <g class="cover__corners" fill="var(--gold-mid)" opacity="0.55">
    <circle role="img" aria-label="Gold corner flourish" cx="118" cy="106" r="20"/>
    <circle role="img" aria-label="Gold corner flourish" cx="1080" cy="106" r="20"/>
    <circle role="img" aria-label="Gold corner flourish" cx="118" cy="657" r="20"/>
    <circle role="img" aria-label="Gold corner flourish" cx="1080" cy="657" r="20"/>
  </g>

  <!-- title -->
  <text class="cover__title" x="171" y="415" textLength="864" lengthAdjust="spacingAndGlyphs"
        fill="url(#gold-sheen)">FAMILY</text>

  <!-- dedication line -->
  <g class="cover__dedication-row" fill="url(#gold-sheen)">
    <path class="cover__diamond" d="M192 484 L212 504 L192 524 L172 504 Z"/>
    <text class="cover__dedication" x="225" y="523" textLength="758" lengthAdjust="spacingAndGlyphs">TO OUR HARLOW FAIRWAY</text>
    <path class="cover__diamond" d="M1018 484 L1038 504 L1018 524 L998 504 Z"/>
  </g>
</svg>
</body>
</html>
```